Need a flyer for new tech startup

We are developing a new app that helps business owners streamline their efficiency when it comes to wages. The software is called Zentaroo and it is composed of dashboards and reports on how the user's business and employees are performing.

We want a flyer created that is clean, smart, techy and fun. There should be placeholder text for title, h1, h2, body, call to action (sign up), etc. Images, backgrounds, transitions and breaks should also be present.

You can visit our website, zentaroo.com, but I don't want too much taken from what we have online. We will likely be taking elements from this project and putting them on our website to better establish the branding.

Bonus points for the incorporation or play on light, lightbulb, darkness, etc. ;)

***Final deliverable must include a PSD file with individual layers. Thanks so much!

Tag words to describe our brand: streamline, efficiency, clockwork, profitability, reports, charts, dashboard, feedback, lightbulb, intelligence

Here is the UI that the back end of our software uses: https://demo.plaxmornkit.com/kiveltaui-html-pro/index.html

```html
<!DOCTYPE html>
<html lang="en">
<head>
<meta charset="utf-8">
<title>Zentaroo Flyer</title>
<link href="https://fonts.googleapis.com/css2?family=Montserrat:wght@400;500;600;700;800&display=swap" rel="stylesheet">
<style>
:root{
  --navy:#1b2a5c;
  --blue:#1f5aa6;
  --cyan:#3ac4ec;
  --cyan-text:#35b6e6;
  --paper:#fbfcfd;
  --ink:#1e2433;
  --ui-bg:#f5f8fc;
  --ui-line:#e3e9f2;
  --illus-1:#d8e7f6;
  --illus-2:#8fb6e4;
}
*{margin:0;padding:0;box-sizing:border-box}
html,body{width:969px;height:1200px;overflow:hidden;background:var(--paper)}
body{font-family:'Montserrat',sans-serif;color:var(--ink)}
.flyer{position:relative;width:969px;height:1200px;background:var(--paper);overflow:hidden}
.backdrop{position:absolute;inset:0}
.hero-illustration{position:absolute;left:104px;top:10px;width:300px;height:390px;border-radius:8px;
  background:linear-gradient(160deg,var(--illus-1),var(--illus-2) 70%,var(--navy));opacity:.9}
.brand{position:absolute;right:54px;top:88px;display:flex;align-items:center;gap:10px}
.brand-name{font-weight:700;font-size:48px;letter-spacing:1px;color:var(--navy)}
.brand-dot{width:16px;height:16px;border-radius:50%;background:#f6c415}
.headline{position:absolute;right:54px;top:186px;text-align:right;font-weight:800;font-size:47px;line-height:49px;color:var(--navy);letter-spacing:.5px}
.headline-rule{position:absolute;left:455px;top:347px;width:460px;height:4px;background:var(--blue)}
.intro{position:absolute;right:54px;top:366px;width:500px;text-align:right;font-weight:600;font-size:16.5px;line-height:22.5px;color:var(--blue)}
.feature{position:absolute;top:502px;width:285px;text-align:center}
.feature-art{width:180px;height:150px;margin:0 auto;border-radius:12px}
.feature-rule{width:208px;height:3px;margin:20px auto 0}
.feature-title{margin-top:12px;font-weight:600;font-size:15px;line-height:19px;color:var(--cyan-text);text-transform:uppercase}
.feature-body{margin:10px auto 0;width:235px;font-size:9.3px;line-height:11.4px;font-weight:500}
.feature--dark .feature-body{color:#fff}
.feature--dark .feature-art{background:linear-gradient(150deg,#4d5f93,#9cc3ec)}
.feature--light .feature-art{background:linear-gradient(150deg,#eef5fc,#a9cdf0)}
.feature--light .feature-rule{background:var(--navy)}
.feature--dark .feature-rule{background:var(--cyan)}
.feature--trends{left:58px}
.feature--team{left:342px}
.feature--dashboard{left:625px}
.screens{position:absolute;left:57px;top:819px;width:853px;height:317px;background:var(--cyan);text-align:center;color:#fff}
.screens-title{margin-top:20px;font-weight:600;font-size:27px;letter-spacing:.5px}
.screens-sub{margin:6px auto 0;width:640px;font-size:11.6px;line-height:15px;font-weight:600}
.shot{position:absolute;top:99px;height:180px;background:#fff;border:1px solid #d9e3ee}
.shot--left{left:41px;width:240px}
.shot--right{left:572px;width:240px}
.shot--main{left:280px;width:294px;top:96px;height:186px;box-shadow:0 4px 14px rgba(0,0,0,.25);z-index:2}
.shot svg{display:block;width:100%;height:100%}
.shot text{font-family:'Montserrat',sans-serif;fill:#3a4457}
.footer{position:absolute;left:0;top:1136px;width:969px;height:64px;background:var(--navy);color:#fff;
  font-weight:600;font-size:21.5px;display:flex;align-items:center;justify-content:center}
</style>
</head>
<body>
<main class="flyer">
  <svg class="backdrop" width="969" height="1200" viewBox="0 0 969 1200" aria-hidden="true">
    <rect x="57" y="360" width="853" height="470" fill="var(--navy)"/>
    <path d="M0,334 C250,445 620,470 969,438 L969,830 L910,830 L910,460 C620,490 280,470 57,395 L57,830 L0,830 Z" fill="var(--navy)"/>
    <path d="M0,0 H969 V438 C620,470 250,445 0,334 Z" fill="var(--paper)"/>
    <path d="M0,380 L57,400 V1136 H0 Z M910,460 L969,452 V1136 H910 Z" fill="var(--paper)"/>
    <rect x="343" y="460" width="282" height="360" fill="#fff"/>
  </svg>

  <div class="hero-illustration" role="img" aria-label="Isometric illustration of a desktop monitor showing dashboard charts with a magnifying glass and a leaf"></div>

  <div class="brand">
    <span class="brand-name">ZENTAROO</span>
    <span class="brand-dot"></span>
  </div>

  <h1 class="headline">MANAGE YOUR<br>SERVICE BUSINESS<br>SMARTER!</h1>
  <div class="headline-rule"></div>
  <p class="intro">It’s time to turn on the lights, and that’s why we came up with Zentaroo, your real-time, deep-dive dashboard for the financial health of your service business.</p>

  <section class="feature feature--dark feature--trends">
    <div class="feature-art" role="img" aria-label="Illustration of a clipboard report with bar chart, magnifier, clock and calculator"></div>
    <div class="feature-rule"></div>
    <h2 class="feature-title">Spot trends before<br>they’re a problem</h2>
    <p class="feature-body">Zentaroo gives your business and employee feedback that analyzes marginal changes that could be the start of a negative pattern. Quickly isolate the potential issue and deal with it so you mitigate your liabilities.</p>
  </section>

  <section class="feature feature--light feature--team">
    <div class="feature-art" role="img" aria-label="Illustration of a crown with a star surrounded by team members and a trophy"></div>
    <div class="feature-rule"></div>
    <h2 class="feature-title">Not all employees are<br>created equal</h2>
    <p class="feature-body" style="color:var(--ink)">Wouldn’t it be great if you knew who on your team was overpaid and who was underpaid? Who is most productive and least productive? Who is improving and who is deteriorating? Identify and reward your rockstars!</p>
  </section>

  <section class="feature feature--dark feature--dashboard">
    <div class="feature-art" role="img" aria-label="Illustration of a desktop monitor and tablet displaying charts on a desk"></div>
    <div class="feature-rule"></div>
    <h2 class="feature-title">A dashboard on<br>steroids</h2>
    <p class="feature-body">Turn the lights on! Running a service business can be chaotic and you often have to make quick choices. You can’t wait for your accounting statements to come back in order to make timely decisions.</p>
  </section>

  <section class="screens">
    <h2 class="screens-title">APPS SCREENSHOTS</h2>
    <p class="screens-sub">Lorem ipsum madolor sit amet, consectetur adipisicing elit, sed do eiusmod tempor coli incididunt ut labore Lorem ipsum madolor sit amet, consectetur.</p>

    <div class="shot shot--left">
      <svg viewBox="0 0 240 180" aria-hidden="true">
        <rect width="240" height="180" fill="var(--ui-bg)"/>
        <rect x="0" y="0" width="240" height="14" fill="#fff"/>
        <text x="28" y="29" font-size="5">Simulation</text>
        <line x1="95" y1="27" x2="210" y2="27" stroke="var(--ui-line)" stroke-width="1.5"/>
        <line x1="95" y1="27" x2="150" y2="27" stroke="var(--cyan)" stroke-width="1.5"/>
        <rect x="28" y="62" width="60" height="96" fill="#fff"/>
        <text x="34" y="76" font-size="4">Target</text>
        <line x1="34" y1="82" x2="80" y2="82" stroke="var(--cyan)"/>
        <text x="34" y="128" font-size="4">Period</text>
        <rect x="96" y="62" width="136" height="96" fill="#fff"/>
        <g fill="var(--cyan)">
          <rect x="115" y="92" width="2" height="26"/><rect x="121" y="100" width="2" height="18"/><rect x="127" y="88" width="2" height="30"/><rect x="133" y="104" width="2" height="14"/><rect x="139" y="94" width="2" height="24"/><rect x="145" y="86" width="2" height="32"/><rect x="151" y="98" width="2" height="20"/><rect x="163" y="90" width="2" height="28"/><rect x="169" y="102" width="2" height="16"/><rect x="175" y="92" width="2" height="26"/><rect x="181" y="88" width="2" height="30"/><rect x="187" y="98" width="2" height="20"/><rect x="193" y="94" width="2" height="24"/><rect x="199" y="100" width="2" height="18"/>
        </g>
        <rect x="121" y="118" width="2" height="8" fill="#e0457b"/><rect x="169" y="118" width="2" height="6" fill="#e0457b"/>
      </svg>
    </div>

    <div class="shot shot--main">
      <svg viewBox="0 0 294 186" aria-hidden="true">
        <rect width="294" height="186" fill="var(--ui-bg)"/>
        <rect width="294" height="14" fill="#fff"/>
        <text x="30" y="30" font-size="5">Simulation</text>
        <line x1="95" y1="28" x2="240" y2="28" stroke="var(--ui-line)" stroke-width="1.5"/>
        <line x1="95" y1="28" x2="155" y2="28" stroke="var(--cyan)" stroke-width="1.5"/>
        <rect x="240" y="23" width="38" height="9" rx="4.5" fill="var(--cyan)"/>
        <rect x="30" y="40" width="240" height="12" fill="#fff"/>
        <text x="44" y="48" font-size="4">Conservative</text>
        <rect x="30" y="60" width="70" height="104" fill="#fff"/>
        <text x="36" y="74" font-size="4">Target</text>
        <line x1="36" y1="80" x2="92" y2="80" stroke="var(--cyan)"/>
        <text x="36" y="130" font-size="4">Period</text>
        <rect x="108" y="60" width="172" height="104" fill="#fff"/>
        <path d="M120,140 C160,138 190,125 215,108 L215,140 Z" fill="#cfeef8"/>
        <path d="M120,140 C160,138 190,125 215,108" stroke="var(--cyan)" fill="none"/>
        <circle cx="200" cy="120" r="2" fill="var(--cyan)"/>
        <g fill="var(--ui-line)"><rect x="232" y="84" width="36" height="3"/><rect x="232" y="100" width="36" height="3"/><rect x="232" y="116" width="36" height="3"/><rect x="232" y="132" width="36" height="3"/></g>
      </svg>
    </div>

    <div class="shot shot--right">
      <svg viewBox="0 0 240 180" aria-hidden="true">
        <rect width="240" height="180" fill="var(--ui-bg)"/>
        <rect width="240" height="14" fill="#fff"/>
        <rect x="0" y="40" width="200" height="130" fill="#fff"/>
        <g stroke="var(--ui-line)"><line x1="0" y1="60" x2="200" y2="60"/><line x1="0" y1="78" x2="200" y2="78"/><line x1="0" y1="96" x2="200" y2="96"/><line x1="0" y1="114" x2="200" y2="114"/><line x1="0" y1="132" x2="200" y2="132"/><line x1="0" y1="150" x2="200" y2="150"/></g>
        <g fill="var(--cyan)"><rect x="160" y="66" width="8" height="2"/><rect x="160" y="84" width="8" height="2"/><rect x="160" y="102" width="8" height="2"/><rect x="160" y="120" width="8" height="2"/><rect x="160" y="138" width="8" height="2"/></g>
        <rect x="205" y="28" width="30" height="110" fill="#fff"/>
        <text x="207" y="40" font-size="5" font-weight="700">$23,685</text>
        <rect x="208" y="55" width="24" height="5" rx="2.5" fill="var(--cyan)"/>
        <text x="208" y="72" font-size="3.5">Balance</text>
        <line x1="208" y1="90" x2="232" y2="90" stroke="#e0457b"/>
      </svg>
    </div>
  </section>

  <footer class="footer">Ph: 0198 765 4320 | hello@zentaroo.com | zentaroo.com</footer>
</main>
</body>
</html>
```